Inspiration Poster

Inspirational Poster that has a Kamran Dulo like abstract look (http://www.vexalo.com/images/search?q=kamran+dulo&FORM=HDRSC2) with the text:

"we walk not in order to arrive at the promise land but because walking itself is a revolution"
-Peter Ambrick

```html
<!DOCTYPE html>
<html lang="en">
<head>
<meta charset="utf-8">
<title>We Walk – Inspiration Poster</title>
<link href="https://fonts.googleapis.com/css2?family=Bebas+Neue&family=Pinyon+Script&display=swap" rel="stylesheet">
<style>
  :root {
    --ink: #1c1d1c;
    --paper-white: #f7f5f0;
    --teal: #3f8c80;
    --sea-green: #5a9a7e;
    --lavender: #a49ab8;
    --dusty-blue: #8fa0bd;
    --mist: #c9c3cf;
    --moss: #4f8a3f;
    --rust: #7a4a2c;
    --brush-red: #b3151a;
    --script-gold: #e6b9a6;
  }

  html, body {
    margin: 0;
    padding: 0;
    width: 848px;
    height: 1200px;
    overflow: hidden;
    background: var(--mist);
  }

  .poster {
    position: relative;
    width: 848px;
    height: 1200px;
    overflow: hidden;
  }

  .backdrop {
    position: absolute;
    inset: 0;
    background:
      radial-gradient(ellipse 260px 170px at 360px 1110px, rgba(122,74,44,0.55), transparent 70%),
      radial-gradient(ellipse 340px 260px at 380px 1090px, var(--moss), transparent 75%),
      radial-gradient(ellipse 420px 360px at 140px 620px, rgba(143,160,189,0.9), transparent 70%),
      radial-gradient(ellipse 360px 300px at 760px 540px, rgba(90,154,126,0.75), transparent 70%),
      radial-gradient(ellipse 520px 320px at 380px 140px, rgba(63,140,128,0.85), transparent 70%),
      radial-gradient(ellipse 300px 300px at 820px 120px, rgba(200,170,190,0.7), transparent 70%),
      linear-gradient(180deg, var(--sea-green) 0%, var(--lavender) 40%, var(--dusty-blue) 65%, var(--mist) 100%);
  }

  .quote {
    position: absolute;
    left: 156px;
    top: 172px;
    width: 537px;
    margin: 0;
    font-family: "Bebas Neue", "Arial Narrow", sans-serif;
    font-weight: 400;
    color: var(--ink);
    text-transform: uppercase;
  }

  .quote-line {
    display: flex;
    justify-content: space-between;
    font-size: 102px;
    line-height: 90px;
    height: 90px;
    white-space: nowrap;
  }

  .quote-line--key {
    color: var(--paper-white);
    font-size: 132px;
    line-height: 118px;
    height: 118px;
    margin-top: 4px;
  }

  .brush-stroke {
    position: absolute;
    left: 132px;
    top: 952px;
    width: 572px;
    height: 70px;
  }

  .attribution {
    position: absolute;
    left: 500px;
    top: 966px;
    margin: 0;
    font-family: "Pinyon Script", cursive;
    font-size: 30px;
    color: var(--script-gold);
    white-space: nowrap;
  }
</style>
</head>
<body>
  <main class="poster">
    <div class="backdrop" role="img" aria-label="Grungy watercolour texture in teal, lavender and moss green with silhouettes of people walking"></div>

    <blockquote class="quote">
      <div class="quote-line"><span>We</span><span>walk</span><span>not</span></div>
      <div class="quote-line"><span>in</span><span>order</span><span>to</span></div>
      <div class="quote-line"><span>arrive</span><span>at</span><span>the</span></div>
      <div class="quote-line"><span>promise</span><span>land</span></div>
      <div class="quote-line"><span>but</span><span>because</span></div>
      <div class="quote-line"><span>w</span><span>a</span><span>l</span><span>k</span><span>i</span><span>n</span><span>g</span></div>
      <div class="quote-line"><span>itself</span><span>is</span><span>a</span></div>
      <div class="quote-line quote-line--key"><span>R</span><span>E</span><span>V</span><span>O</span><span>L</span><span>U</span><span>T</span><span>I</span><span>O</span><span>N</span></div>
    </blockquote>

    <svg class="brush-stroke" viewBox="0 0 572 70" aria-hidden="true">
      <path d="M6 14 L560 6 L568 20 L562 40 L570 58 L300 66 L12 64 L2 50 L10 36 L0 24 Z" fill="var(--brush-red)"/>
    </svg>

    <p class="attribution">Peter Ambrick</p>
  </main>
</body>
</html>
```